Booklet for meditation CD to match existing CD cover

We need a design for a booklet that matches the meditation CD cover previously designed. It should look like it belongs to the CD as it will be inserted into the cover slot. I hope you can re-use some of the existing artwork. It should incorporate the logo and the text and probably the list of tracks as well. I have attached the original CD cover file, the logo file, photo file and the specs from the CD production company for the 8 page booklet. The spec also includes a cover spec. You can ignore that part. Please put all the text from the CD cover, as well as the track names and the credits from the CD cover into the booklet and the text describing the meditation in full which I have enclosed as a word file.

Target Market(s)

People interested in meditation and personal growth

Font styles to use
Serif

Colors
0555a3
876aae
a54499
e667a6
ee363c

Requirements
Must have
• must match the existing CD cover, must include logo and photo and text from CD cover
• Design, Fonts and colours should match CD cover.

```html
<!DOCTYPE html>
<html lang="en">
<head>
<meta charset="utf-8">
<title>Meditation Booklet – Inner Pages</title>
<link href="https://fonts.googleapis.com/css2?family=Roboto+Condensed:ital,wght@1,300;1,400;1,700&display=swap" rel="stylesheet">
<style>
  :root{
    --ink:#2b1c38;
    --frame:#2a1f33;
    --sky-top:#6e5384;
    --sky-mid:#a98aa8;
    --sky-low:#e9cbd6;
    --dusk-top:#7d5c9c;
    --dusk-mid:#d86aa8;
    --dusk-low:#e99bc2;
    --sea:#a54499;
    --page:#ffffff;
  }
  html,body{margin:0;padding:0;width:1200px;height:1200px;overflow:hidden;background:var(--page);}
  body{font-family:"Roboto Condensed",sans-serif;font-style:italic;color:var(--ink);position:relative;}
  .panel{position:absolute;width:578px;height:572px;overflow:hidden;}
  .panel--tl{left:23px;top:20px;}
  .panel--tr{left:602px;top:20px;}
  .panel--bl{left:23px;top:602px;}
  .panel--br{left:600px;top:602px;}
  .sky{position:absolute;inset:0;
    background:linear-gradient(180deg,var(--sky-top) 0%,var(--sky-mid) 50%,var(--sky-low) 100%);}
  .dusk{position:absolute;inset:0;
    background:linear-gradient(180deg,var(--dusk-top) 0%,var(--dusk-mid) 40%,var(--dusk-low) 72%,var(--sea) 100%);}
  .frame{position:absolute;inset:11px;border:3px double var(--frame);}
  .content{position:absolute;inset:18px 18px 12px 18px;text-align:center;font-size:13.2px;line-height:16px;font-weight:300;}
  .content h2{font-size:13.4px;font-weight:700;margin:0 0 6px;line-height:16px;}
  .content h3{font-size:13.4px;font-weight:700;margin:14px 0 14px;line-height:16px;}
  .content p{margin:0;}
  .intro{position:absolute;left:26px;right:26px;top:22px;text-align:center;font-size:13.2px;line-height:16px;font-weight:300;}
  .intro p{margin:0 0 16px;}
  .tracks{position:absolute;left:104px;width:354px;top:132px;list-style:none;margin:0;padding:0;font-weight:700;font-size:13px;line-height:16px;}
  .tracks li{display:flex;align-items:baseline;}
  .tracks .num{width:26px;}
  .tracks .name{white-space:nowrap;}
  .tracks .lead{flex:1;border-bottom:2px dotted var(--ink);margin:0 1px 3px;}
  .quote{position:absolute;left:110px;right:110px;top:472px;margin:0;text-align:center;font-weight:700;font-size:13px;line-height:16px;}
  .signature{position:absolute;right:126px;top:515px;margin:0;font-weight:700;font-size:13px;}
</style>
</head>
<body>

<section class="panel panel--tl">
  <div class="sky" role="img" aria-label="Photo: starry purple night sky fading to a soft pink glow with birds in flight"></div>
  <div class="frame"></div>
  <div class="content">
    <h2>Fourth stage: Journeying up through each of the energy centres or chakras in the body</h2>
    <h3 style="margin-top:16px;margin-bottom:0">Focusing:</h3>
    <p>Begin by focusing all the energy in your body down at the base of your body. Imagine white light energy streaming down from your head, from your fingers, from your feet down into the base of your body, the first chakra. Use your breath – like you would use breath to start a fire, giving the fire more oxygen, more air, to bring your inner fire alive. Imagine you could breathe through the base of your trunk. You can guide the energy by visualizing it moving in your body or by sensing it and guiding it, or by physically stroking your body as if you were sweeping the energy to the base of your body.</p>
    <h3>1st chakra: Instinct - nature</h3>
    <p>You are bringing your total focus to the centre of instinct that sits at the base of your trunk. We’re going on a journey through the chakras or energy centres of your body. Even if this is unfamiliar to you, allow yourself to focus your attention in each centre or chakra and imagine your breath is going there. The centre of instinct is at the very base of your body. It is associated with primal energy, an energy that wants to become life, that wants to live. It has a raw quality to it. Think of a lioness protecting her young or animals mating. It is pure instinct. It doesn’t have any reflection or consideration in it. It’s the beginning stage of life happening.</p>
    <h3>2nd chakra: Sacral - sex</h3>
    <p>From there we move the energy up into the sacral centre. This is focused on your sexual nature, your wanting and reaching out to get what you want and to get pleasure. Breathing and focusing on the area of your sex will help you connect with this. There is nothing to do with the energy, just notice the life that is happening there and let it have its natural movement.</p>
    <h3>3rd chakra: Naval - power</h3>
    <p>Then we move up to the centre of power. This is the area sometimes known as the hara in martial arts. It’s just below the belly button. As you breathe and focus on this area you can connect with your own personal power, the power to stand in your own being as a man or woman and feel your strength there. Let yourself move to standing during this section if you have been down on the mattress or floor. Feel yourself standing on the ground on your human journey as man or woman.</p>
  </div>
</section>

<section class="panel panel--tr">
  <div class="sky" role="img" aria-label="Photo: starry purple night sky fading to a soft pink glow with birds in flight"></div>
  <div class="frame"></div>
  <div class="content">
    <h2 style="margin-bottom:14px">4th chakra: Heart</h2>
    <p>The fourth centre is the heart chakra. Focus on your heart with your breath. Imagine and feel all the wild energies from the lower centres flowing up into your heart and your heart transforming all this wild crazy passionate energy into a calm, loving radiance that fills you and surrounds you giving you a sense of a deeper inner yes to yourself. Bask in this deep inner yes to yourself that the heart centre gives you when you tune in to it and allow it to receive you in your totality. Feel into the boundlessness of your heart and its capacity to hold you, embrace you. Feel how your heart is so much greater than your wounds. And as you connect with your heart energy, feel the sense of an inner mother holding you, the mother of great compassion embracing you. Relax into this and receive this loving energy.</p>
    <h3>5th chakra: Throat</h3>
    <p>This deep inner yes to yourself moves up into your throat centre, the centre of your unique expression of being. It brings a yes to your voice, to your way of being and living yourself so that you can bring your gifts to the world. Feel into the freedom to live and give of yourself without fear, without censoring yourself, knowing you are good enough. Trusting that your gift is uniquely yours to give and is welcomed by existence.</p>
    <h3>6th chakra: Third Eye - Intuition</h3>
    <p>And then let that energy of a yes to your being flow up into the centre of intuition, the point between your eyebrows. It’s the gateway beyond your physical self, sometimes felt as a deep inner knowing or being in touch with divine wisdom. The more you pay attention to this point, entering into a deep listening, the more you will receive. Don’t worry if you don’t feel anything at first. It’s a practice and it may be a sense that you haven’t used in a while. Enter with curiosity into the possibility.</p>
    <h3>7th chakra: Crown</h3>
    <p style="line-height:13.5px;font-size:12.8px">Whatever you find, you let that energy also move upwards to the crown of your head or just above it. Allow your attention to expand out beyond yourself, allowing that connection with spirit that at some level you have known since the beginning of time. You may have had glimpses of this ground of consciousness that is beyond the physical realm. Allow yourself to be still, melting into this ethereal state just as a drop of rain dissolves into the ocean. Enter One-ness. No doing, no trying. Simply being with whatever arises as you allow your consciousness to expand.</p>
  </div>
</section>

<section class="panel panel--bl">
  <div class="sky" role="img" aria-label="Photo: starry purple night sky fading to a soft pink glow with birds in flight"></div>
  <div class="frame"></div>
  <div class="content">
    <h2>Fifth Stage - Receiving the energy of the infinite</h2>
    <p style="margin-top:14px">And standing in that consciousness and giving yourself the delicious gift of complete stillness without any movement for two minutes.</p>
    <h3>Sixth Stage: You are guided back, grounding all this energy down into your physical body</h3>
    <p>Your body still alive from the earlier stages of your journey and still open to receive and be enriched by the Source of existence. Allow that flow of energy to enrich and enlighten your physical body, opening each centre in turn: your third eye, your throat, your heart, your power centre, your sex and your root chakra. Allow this flow of Spirit back into your being and into the earth beneath your feet, feeling yourself one part of the infinite flow of existence. And feel the flow of your nature rising up to meet Spirit in one eternal, never ending cycle. Stay alive to all that is moving in you and find your way into sitting in stillness.<br>Sitting in meditation for 15 minutes.</p>
    <p>A word about sitting. To get the most out of any silent sitting meditation, it is recommended that you keep your spine upright as if there were an invisible thread from the crown of your head pulling upwards while your body remains relaxed. It is more important to be comfortable than to contort your body or force it into a position that doesn’t let you relax. Ideally you will have three points making contact with the floor. If you know how to sit in the lotus position and can relax there, that’s wonderful. If you can sit cross-legged supported by a cushion with both knees touching the floor, that works well. If you are balancing on your sit bones with nothing else to support you, you’re probably going to end slumping. In that case, it is usually better to either sit against a wall or sit in a chair or stand. With an upright spine you are holding yourself between total relaxation and total attention so that you could spring up like a samurai warrior.</p>
    <p>As you sit silently listening to all the life that flows within you, you may find it helpful to keep your attention on your breath. In any case, any time you find yourself lost in some thought, simply let go and bring yourself back to this present moment.</p>
    <h3>Seventh stage - Celebration and returning to your day</h3>
    <p>Finally, as the music brings you back to end your meditation, allow it to call you into the beauty of this moment, into a celebration of life and all that it gives you, and especially into a celebration of this wholeness, this totality of being that you are, here, now today. Take this out into your day.</p>
  </div>
</section>

<section class="panel panel--br">
  <div class="dusk" role="img" aria-label="Photo: lone tree silhouetted against a sunset over a calm sea under a pink sky"></div>
  <div class="intro">
    <p>We developed this meditation primarily to be used in workshops as the morning meditation but it can also be used very effectively at home. You may need to use pillows to muffle the sounds during the wild phase. The aim is to bring you into your body, connecting you through movement with both your physical and emotional body and then using that vital and alive connection to open to an experience of Essence.</p>
    <p>If you want to find out more about workshops with Mira Lund, go to www.miralund.com</p>
  </div>
  <ol class="tracks">
    <li><span class="num">1.</span><span class="name">Shaking</span><span class="lead"></span><span>6:56</span></li>
    <li><span class="num">2.</span><span class="name">The flow of your wild energy</span><span class="lead"></span><span>6:54</span></li>
    <li><span class="num">3.</span><span class="name">Loving yourself</span><span class="lead"></span><span>5:51</span></li>
    <li><span class="num">4.</span><span class="name">Focussing the energy</span><span class="lead"></span><span>1:14</span></li>
    <li><span class="num">5.</span><span class="name">Centre of instinct</span><span class="lead"></span><span>1:47</span></li>
    <li><span class="num">6.</span><span class="name">Sacral Chakra</span><span class="lead"></span><span>1:57</span></li>
    <li><span class="num">7.</span><span class="name">Power Centre</span><span class="lead"></span><span>2:02</span></li>
    <li><span class="num">8.</span><span class="name">Heart Chakra</span><span class="lead"></span><span>2:47</span></li>
    <li><span class="num">9.</span><span class="name">Throat Chakra</span><span class="lead"></span><span>2:26</span></li>
    <li><span class="num">10.</span><span class="name">Centre of Intuition</span><span class="lead"></span><span>2:08</span></li>
    <li><span class="num">11.</span><span class="name">Crown Chakra</span><span class="lead"></span><span>1:56</span></li>
    <li><span class="num">12.</span><span class="name">Silence</span><span class="lead"></span><span>2:00</span></li>
    <li><span class="num">13.</span><span class="name">Receiving the infinite</span><span class="lead"></span><span>5:04</span></li>
    <li><span class="num">14.</span><span class="name">Silence</span><span class="lead"></span><span>15:00</span></li>
    <li><span class="num">15.</span><span class="name">Celebration of Being</span><span class="lead"></span><span>4:08</span></li>
  </ol>
  <p class="quote">“ Grounded in your nature, inspired by the light and with your heart´s open eyes to all that you are, feel the blessing of this life. “</p>
  <p class="signature">MIRA LUND</p>
</section>

</body>
</html>
```